New Full Color Flyer for Mailing Program

I have a flyer already for a program I launching. I am in need of a professional to use my flyer to create a much more leaner flyer. The new flyer should convey a message through the use of graphics rather then words.
The goal is to incite the reader to get excited and buy in, but at the same time explain the products that are included with a purchase.
Attached is my own flyer to be used as a reference point. I allow you to make suggestions to me to consider for the flyer and changes you think will perform well.
MUST BE PSD SOURCE & is expected to be handed over at the end.
Target Market(s)
Home business and income opportunity buyers
Industry/Entity Type
Small Business
Colors
Designer to choose colors to be used in the design.
Requirements
Must have
- Exciting Graphics/cartoons that convey success, money and riches. Should look good in color and gray/white.
- Level Payouts
- Order Form
- THE KESTREL VALE ROUTINE
Nice to have
- crisp clean text

```html
<!DOCTYPE html>
<html lang="en">
<head>
<meta charset="utf-8">
<title>Kestrel Vale Routine Flyer</title>
<link href="https://fonts.googleapis.com/css2?family=Anton&family=Open+Sans:ital,wght@0,400;0,600;0,700;0,800;1,600;1,700&display=swap" rel="stylesheet">
<style>
:root{
  --navy:#1b2238;
  --navy-band:#233a78;
  --red:#e0212b;
  --red-deep:#c8161f;
  --white:#ffffff;
  --grey:#c9c9c9;
  --ink:#1d1d1d;
  --page:#ececec;
  --dash:rgba(255,255,255,.75);
}
*{box-sizing:border-box;margin:0;padding:0}
html,body{width:1020px;height:1200px;overflow:hidden}
body{background:var(--page);font-family:"Open Sans",Arial,sans-serif;position:relative}
.flyer{position:absolute;left:99px;top:20px;width:822px;height:1160px;background:var(--navy);overflow:hidden;color:var(--white)}
.abs{position:absolute}

.masthead{left:0;top:0;width:822px;height:121px;background:linear-gradient(180deg,#f0353d,var(--red-deep));text-align:center}
.masthead h1{font-family:"Anton",Impact,sans-serif;font-weight:400;font-size:50px;letter-spacing:1px;line-height:1;padding-top:14px;color:var(--white);text-shadow:2px 3px 2px rgba(0,0,0,.45)}
.masthead p{font-weight:700;font-size:22px;color:#1a1a1a;margin-top:8px}

.headline{left:110px;top:142px;width:590px;height:80px;background:var(--white);text-align:center;
  clip-path:polygon(0 6%,3% 0,20% 4%,40% 1%,62% 5%,85% 0,100% 4%,99% 50%,100% 96%,80% 100%,60% 95%,38% 100%,15% 96%,2% 100%,1% 55%)}
.headline .l1{display:block;color:var(--red);font-weight:800;font-size:26px;padding-top:6px;line-height:1.3}
.headline .l2{display:block;color:var(--ink);font-weight:800;font-size:26px;line-height:1.25}

.intro{left:40px;top:240px;width:742px;font-size:14px;line-height:20px;text-align:center}

.panel{top:313px;height:253px;border:2px dashed var(--dash);border-radius:14px;padding:12px 14px}
.panel-limits{left:62px;width:331px}
.panel-pay{left:421px;width:341px}
.panel h2{color:var(--red);font-weight:800;font-size:19px;line-height:1.2}
.limits-body{display:flex;margin-top:14px;gap:4px}
.limits-body p{font-weight:700;font-size:13.5px;line-height:19px;width:114px;flex:none}
.levels{list-style:none;font-weight:700;font-size:13.5px;line-height:22px;position:relative;padding-left:32px;margin-top:-1px;white-space:nowrap}
.levels em{font-style:normal;color:var(--red)}
.levels svg{position:absolute;left:0;top:25px}
.panel-pay p{font-size:13px;line-height:18.5px;margin-top:6px}
.ticks{list-style:none;margin-top:8px}
.ticks li{font-weight:700;font-size:13px;line-height:19.5px;display:flex;align-items:center;gap:10px}

.start{left:0;top:573px;width:331px;height:96px;background:var(--red);text-align:center;font-weight:800;font-size:20px;line-height:28px;padding-top:20px}
.bar{left:0;width:331px;background:var(--navy-band);font-weight:700;text-align:center}
.bar-select{top:669px;height:22px;font-size:17px;line-height:22px}
.tiers{left:0;top:691px;width:331px;list-style:none}
.tiers li{height:59px;padding:4px 14px 0 20px;color:var(--ink);font-weight:700;font-size:12px;line-height:16px}
.tiers li:nth-child(odd){background:var(--grey)}
.tiers li:nth-child(even){background:var(--white)}
.tiers b{display:block;color:var(--red);font-weight:800;font-size:17px;line-height:22px;white-space:nowrap}
.tiers i{font-style:normal;color:var(--red)}
.bar-note{top:986px;height:26px;font-size:13px;line-height:26px;font-weight:600;text-align:left;padding-left:20px}
.question{left:0;top:1012px;width:331px;height:64px;background:var(--white);color:var(--ink);text-align:center;font-weight:700;font-size:16px;line-height:22px;padding-top:9px}
.leads{left:0;top:1076px;width:331px;height:42px;background:var(--red);text-align:center;font-weight:700;font-size:17px;line-height:42px}
.disclaimer{left:18px;top:1126px;width:790px;color:var(--red);font-style:italic;font-size:11px;line-height:14px;font-weight:600}

.ribbon{background:var(--red);text-align:center;font-weight:800;color:var(--white);
  clip-path:polygon(0 0,100% 0,96% 50%,100% 100%,0 100%,4% 50%)}
.ribbon-buy{left:393px;top:580px;width:407px;height:34px;font-size:20px;line-height:34px}
.ribbon-reports{left:455px;top:701px;width:290px;height:34px;font-size:20px;line-height:34px}
.includes{left:455px;top:620px;list-style:none}
.includes li{font-size:13px;line-height:18px;display:flex;align-items:center;gap:10px}

.reports{left:331px;top:752px;width:491px;height:116px;background:#eeeeee;color:var(--ink);padding:10px 10px 0 12px;display:grid;grid-template-columns:1fr 1fr;row-gap:6px;column-gap:10px}
.reports div{line-height:14px}
.reports b{display:block;font-weight:800;font-size:14px;white-space:nowrap}
.reports span{display:block;color:var(--red);font-size:10.5px;text-align:center}
.reports .wide{grid-column:1/3;text-align:center}

.order{left:338px;top:874px;width:476px;height:244px;border:2px dashed var(--dash);border-radius:10px;padding:5px 10px 0 12px}
.order h3{color:var(--red);font-style:italic;font-weight:700;font-size:11px;line-height:16px;white-space:nowrap;text-align:center}
.join{display:grid;grid-template-columns:1fr 1fr;font-weight:700;font-size:9.5px;line-height:14px;margin-top:1px;padding-left:6px}
.join .c{grid-column:1/3;text-align:center}
.members{margin:6px 0 0 30px;font-size:12px;line-height:18px}
.members li{padding-left:6px;white-space:nowrap}
.form{margin-top:8px;font-weight:700;font-size:11.5px;line-height:17px;white-space:nowrap;overflow:hidden}
</style>
</head>
<body>
<main class="flyer">
  <header class="masthead abs">
    <h1>KESTREL VALE ROUTINE</h1>
    <p>Quick &amp; Simple Cash Generator</p>
  </header>

  <div class="headline abs">
    <span class="l1">GENERATE ATSUNAMI OF $500 +</span>
    <span class="l2">CASH &amp; MONEY ORDERPAYMENTS DAILY</span>
  </div>

  <p class="intro abs">Kestrel vale routine is an exciting programpaying unlimited commissions to businesses and ordinary joes around the country to resell our online profits how-to reports &amp; training manuals.you just mail this flyer and collect the direct payments.If you can mail a flyer ,this is for you...do not miss this opportunity!</p>

  <section class="panel panel-limits abs">
    <h2>The KESTREL VALE ROUTINE Limits are ENDLESS!!!</h2>
    <div class="limits-body">
      <p>LOOK!!!The $500 Program rewards Handsomly.Based on 10 who get 10</p>
      <ul class="levels">
        <svg width="26" height="14" viewBox="0 0 30 16"><path d="M0 5h20V0l10 8-10 8v-5H0z" fill="#e0212b"/></svg>
        <li>Level 1 =<em>$5,000</em></li>
        <li>Level 2 =<em>$50,000</em></li>
        <li>Level 3 =<em>$500,000</em></li>
        <li>Level 4 =<em>$5,000,000</em></li>
      </ul>
    </div>
  </section>

  <section class="panel panel-pay abs">
    <h2>ENDLESS PAY PLAN</h2>
    <p>You are paid commissions on 4 Levels and your name will continue to be put onto your teams flyers through infinity. Your talking THOUSANDS of flyers with your name making you CASH...That is Power!!!</p>
    <ul class="ticks">
      <li><svg width="12" height="12" viewBox="0 0 12 12"><path d="M1 6l3.5 4L11 1.5" fill="none" stroke="#e0212b" stroke-width="2"/></svg>Affordable Income Opportunity</li>
      <li><svg width="12" height="12" viewBox="0 0 12 12"><path d="M1 6l3.5 4L11 1.5" fill="none" stroke="#e0212b" stroke-width="2"/></svg>Company Support</li>
      <li><svg width="12" height="12" viewBox="0 0 12 12"><path d="M1 6l3.5 4L11 1.5" fill="none" stroke="#e0212b" stroke-width="2"/></svg>Simple To Earn, No monthly free</li>
      <li><svg width="12" height="12" viewBox="0 0 12 12"><path d="M1 6l3.5 4L11 1.5" fill="none" stroke="#e0212b" stroke-width="2"/></svg>Updated and freshProducts</li>
      <li><svg width="12" height="12" viewBox="0 0 12 12"><path d="M1 6l3.5 4L11 1.5" fill="none" stroke="#e0212b" stroke-width="2"/></svg>Unlimited &amp; Direct Payments</li>
    </ul>
  </section>

  <div class="start abs">GET STARTED IN THE<br>KESTREL VALE ROUTINE</div>
  <div class="bar bar-select abs">Select Your Commission Level</div>
  <ul class="tiers abs">
    <li><b>THE KESTREL VALE ROUTINE</b>Unlimited <i>$25</i> Payments</li>
    <li><b>THE KESTREL VALE ROUTINE II</b>Unlimited <i>$50</i> Payments, Includes above level as well</li>
    <li><b>THE KESTREL VALE ROUTINE III</b>Unlimited <i>$100</i> Payments, Includes above level as well</li>
    <li><b>THE KESTREL VALE ROUTINE IV</b>Unlimited <i>$250</i> Payments, Includes above level as well</li>
    <li><b>THE KESTREL VALE ROUTINE V</b>Unlimited <i>$500</i> Payments, Includes above level as well</li>
  </ul>
  <div class="bar bar-note abs">You only commissions upto your puchased level</div>
  <div class="question abs">Question?<br>TKVR@kestrelvaleroutine.net</div>
  <div class="leads abs">Fresh Leads Included-100/leve</div>

  <div class="ribbon ribbon-buy abs">YOUR PURCHASF THE FOLLOWING</div>
  <ul class="includes abs">
    <li><svg width="11" height="11" viewBox="0 0 11 11"><rect x=".5" y=".5" width="10" height="10" fill="none" stroke="#e0212b"/><path d="M2 5.5l2.5 2.5L9 2.5" fill="none" stroke="#e0212b" stroke-width="1.6"/></svg>Fresh Mailing Names on Labels</li>
    <li><svg width="11" height="11" viewBox="0 0 11 11"><rect x=".5" y=".5" width="10" height="10" fill="none" stroke="#e0212b"/><path d="M2 5.5l2.5 2.5L9 2.5" fill="none" stroke="#e0212b" stroke-width="1.6"/></svg>Discounted Campaigns</li>
    <li><svg width="11" height="11" viewBox="0 0 11 11"><rect x=".5" y=".5" width="10" height="10" fill="none" stroke="#e0212b"/><path d="M2 5.5l2.5 2.5L9 2.5" fill="none" stroke="#e0212b" stroke-width="1.6"/></svg>Marketing kit &amp; Quarterly Newsletter</li>
    <li><svg width="11" height="11" viewBox="0 0 11 11"><rect x=".5" y=".5" width="10" height="10" fill="none" stroke="#e0212b"/><path d="M2 5.5l2.5 2.5L9 2.5" fill="none" stroke="#e0212b" stroke-width="1.6"/></svg>License to resell Kestrel Vale Routine</li>
  </ul>
  <div class="ribbon ribbon-reports abs">REPORTS &amp; GUIDES</div>

  <section class="reports abs">
    <div><b>THE KESTREL VALE ROUTINE</b><span>7 Ways tosuccess while you sleep</span></div>
    <div><b>THE KESTREL VALE ROUTINE II</b><span>The Business Guru &amp; TKVR I report</span></div>
    <div><b>THE KESTREL VALE ROUTINE III</b><span>Your money mind 1 TKVR I, II report</span></div>
    <div><b>THE KESTREL VALE ROUTINE IV</b><span>List Building Madness &amp; TKVR I, II, III report</span></div>
    <div class="wide"><b>THE KESTREL VALE ROUTINE V</b><span>Social Feed Training Guide &amp; All Tkvr report</span></div>
  </section>

  <section class="order abs">
    <h3>Send Your:Cash, Money Orders or Cashiers Check to the Below Members</h3>
    <div class="join">
      <span>Join System I &amp; Send each person below $25</span>
      <span>Join SystemIII &amp; send each person below $100</span>
      <span>Join System II &amp; Send each person below $50</span>
      <span>Join SystemIII &amp; send each person below $250</span>
      <span class="c">Join SystemIII &amp; send each person below $500</span>
    </div>
    <ol class="members">
      <li>Dorian Whitcombe 318 Fernhill Rd, Alderbrook CT 06091 1-555-014-2288</li>
      <li>Free Space. No Payment = You Save CASH! :)</li>
      <li>Free Space. No Payment = You Save CASH! :)</li>
      <li>Free Space. No Payment = You Save CASH! :)</li>
      <li>Harbor Post Ventures, PO Box 742, Alderbrook CT 06091 1-555-019-7730</li>
    </ol>
    <div class="form">
      Name........................................................................................................<br>
      Phone..................................................include on flyer (Circle One) yes/no<br>
      Addr....................................City..............................State....................<br>
      Zipcode......................(Use Printed label to prevent any address erroors)
    </div>
  </section>

  <p class="disclaimer abs">Disclaimer:Purch is for reports,Name and marketing hit and licese to be a commissioned affilite for thisoffer.<br>Income example is for illustrative purposes only.No guranteed income.Void where prohibited.</p>
</main>
</body>
</html>
```